KWM Plumbing and Roofing

design a fresh modern card for a young plumbing business looking to break into the market.
Must include the logo in the attached file
Lowen Fairbrook
Phone number 0412689405
Vic Licence no 63920
email......

New Homes & Renovations
General Plumbing & Maintenance
Solar Hot Water Units
Roofing & Guttering (new and replacement)

Industry/Entity Type

Business

```html
<!DOCTYPE html>
<html lang="en">
<head>
<meta charset="utf-8">
<title>KWM Plumbing and Roofing – Business Card</title>
<link rel="stylesheet" href="https://fonts.googleapis.com/css2?family=Arimo:wght@400;700&family=Didact+Gothic&display=swap">
<style>
  :root {
    --backdrop: #e9e7e3;
    --blue-light: #0aa3d6;
    --blue-mid: #0b7fd1;
    --blue-deep: #0a56c0;
    --navy: #0f2d5c;
    --teal: #0aa1bd;
    --ink: #1b1b1b;
    --white: #ffffff;
  }
  * { box-sizing: border-box; margin: 0; padding: 0; }
  html, body { width: 1200px; height: 900px; overflow: hidden; }
  body {
    background: var(--backdrop);
    position: relative;
    font-family: "Arimo", Arial, sans-serif;
  }
  .card {
    position: absolute;
    left: 290px;
    width: 620px;
    height: 362px;
    border-radius: 16px;
    overflow: hidden;
    box-shadow: 0 4px 14px rgba(0,0,0,0.18);
  }
  .card-front {
    top: 70px;
    background: radial-gradient(ellipse at 48% 50%, var(--blue-light) 0%, var(--blue-mid) 45%, var(--blue-deep) 100%);
    display: flex;
    align-items: center;
    justify-content: center;
  }
  .card-back {
    top: 467px;
    height: 363px;
    background: var(--white);
  }
  .brand {
    display: flex;
    align-items: center;
    gap: 14px;
    font-family: "Arimo", Arial, sans-serif;
    font-weight: 700;
  }
  .brand-dot {
    width: 26px; height: 26px;
    border-radius: 50%;
    flex: none;
  }
  .card-front .brand { color: var(--white); font-size: 30px; }
  .card-front .brand-dot { background: var(--white); width: 32px; height: 32px; }
  .card-back .brand {
    position: absolute;
    top: 42px; left: 0; right: 0;
    justify-content: center;
    color: var(--navy);
    font-size: 24px;
  }
  .card-back .brand-dot { background: var(--navy); }
  .services {
    position: absolute;
    top: 132px; left: 0; right: 0;
    text-align: center;
    font-family: "Didact Gothic", Arial, sans-serif;
    font-size: 12.5px;
    letter-spacing: 0.4px;
    line-height: 17px;
    color: var(--ink);
  }
  .service-sep {
    display: inline-block;
    width: 5px; height: 5px;
    border-radius: 50%;
    background: var(--teal);
    margin: 0 5px;
    vertical-align: middle;
  }
  .contact {
    position: absolute;
    top: 221px; left: 0; right: 0;
    text-align: center;
    font-size: 15px;
    line-height: 20px;
    color: var(--ink);
  }
  .contact-name { margin-bottom: 20px; }
  .licence-band {
    position: absolute;
    left: 0; right: 0; bottom: 0;
    height: 43px;
    background: var(--teal);
    display: flex;
    align-items: center;
    justify-content: center;
    font-size: 17px;
    color: var(--ink);
  }
</style>
</head>
<body>
  <section class="card card-front" aria-label="Card front">
    <div class="brand">
      <span class="brand-dot"></span>
      <span class="brand-name">KWM Plumbing and Roofing</span>
    </div>
  </section>

  <section class="card card-back" aria-label="Card back">
    <div class="brand">
      <span class="brand-dot"></span>
      <span class="brand-name">KWM Plumbing and Roofing</span>
    </div>

    <div class="services">
      <p>New Homes &amp; Renovations<span class="service-sep"></span>Solar Hot Water Units</p>
      <p>General Plumbing &amp; Maintenance<span class="service-sep"></span>Roofing &amp; Guttering</p>
    </div>

    <div class="contact">
      <p class="contact-name">Lowen Fairbrook</p>
      <p>T: 0412689405</p>
      <p>E: info@kwmroofing.com</p>
    </div>

    <div class="licence-band">Vic Licence No: 63920</div>
  </section>
</body>
</html>
```